Body corporate management needs business principle flyer design

We need a one page A4 flyer design for our business principles.
We manage body corporates and strata properties.
TenuraKeep is a new initiative for our company. Its a label that we have given to our principles of business that drive our people, systems and processes to give assurance to our clients that every detail matters.
We would like to be able to include this design in future brochure so we are after 1 x portrait and 1 x landscape.
The design needs to portray professionalism.
We would like to see designs that use the colour red. (see attached logo).

Target Market(s)

Professionals

Industry/Entity Type

Business

Font styles to use
Sans Serif

Requirements
Must have
• TenuraKeep logo, provide the design file and as pdf
Nice to have
• the use of the colour red from the logo

```html
<!DOCTYPE html>
<html lang="en">
<head>
<meta charset="utf-8">
<title>TenuraKeep – Principles of Business Flyers</title>
<link href="https://fonts.googleapis.com/css2?family=Open+Sans:wght@400;600;700;800&display=swap" rel="stylesheet">
<style>
  :root{
    --stage:#e9e6e2;
    --ink:#0f0f10;
    --brand:#e8602a;
    --brand-light:#f07a3e;
    --brown-dark:#4e1d0f;
    --brown:#6e2a15;
    --brown-mid:#8a3a1c;
    --gap:#ffffff;
    --paper-text:#ffffff;
  }
  *{box-sizing:border-box;margin:0;padding:0}
  html,body{width:1200px;height:1000px;overflow:hidden}
  body{background:var(--stage);font-family:"Open Sans",Arial,sans-serif;position:relative}

  .flyer{position:absolute;background:var(--gap);box-shadow:0 6px 18px rgba(0,0,0,.25);overflow:hidden}
  .flyer--landscape{left:20px;top:40px;width:690px;height:470px}
  .flyer--portrait{left:735px;top:170px;width:445px;height:640px}

  .masthead{position:absolute;left:0;top:0;width:100%;height:122px;background:var(--ink);color:var(--paper-text)}

  .brand{position:absolute;color:var(--brand);font-weight:400;letter-spacing:-.3px}
  .flyer--landscape .brand{left:28px;top:70px;font-size:25px}
  .flyer--portrait .brand{left:22px;top:74px;font-size:23px}

  .tagline{position:absolute;font-weight:700;line-height:1.22}
  .flyer--landscape .tagline{left:300px;top:28px;width:370px;font-size:14.5px}
  .flyer--portrait .tagline{left:210px;top:34px;width:225px;font-size:13.5px}

  .cell{position:absolute;color:var(--paper-text);padding:6px 8px;font-size:7.2px;line-height:1.38;overflow:hidden}
  .cell h3{font-size:7.8px;font-weight:700;margin-bottom:4px}
  .cell p{text-align:justify}
  .cell--right h3{text-align:right}
  .cell--dark{background:linear-gradient(160deg,var(--brown-dark),var(--brown))}
  .cell--brown{background:linear-gradient(160deg,var(--brown),var(--brown-mid))}
  .cell--orange{background:linear-gradient(160deg,var(--brand),var(--brand-light))}

  .photo{position:absolute}
  .photo--keyboard{background:linear-gradient(135deg,#2a2a2c,#8c8c90 55%,#3a3a3c)}
  .photo--city{background:linear-gradient(180deg,#cfb89a,#8a7a68 45%,#3b3631)}
</style>
</head>
<body>

<section class="flyer flyer--landscape" aria-label="Landscape principles flyer">
  <header class="masthead">
    <div class="brand">TenuraKeep</div>
    <h1 class="tagline">TenuraKeep is our principles of business that drive our people, systems and processes to give assurance to our clients that every detail matters.</h1>
  </header>

  <article class="cell cell--dark cell--right" style="left:0;top:124px;width:171px;height:108px">
    <h3>Client Experience</h3>
    <p>Our promise is to pursue excellence and to continually deliver a solutions based service. We achieve this through active engagement, open channels of communication and a serviced led team with the dedicated resources to listen, engage and implement.</p>
  </article>
  <article class="cell cell--dark" style="left:0;top:234px;width:171px;height:120px">
    <h3>Compliance and Governance</h3>
    <p>We engage and own a position of ‘every detail matters’. We give due diligence to the relevant state and national legislations with which we, our clients and our stakeholders must comply. We regulate and achieve this through a robust system of internal processes and protocols which structure and confirm our deliverables are in line with regulations.</p>
  </article>
  <article class="cell cell--brown cell--right" style="left:0;top:356px;width:171px;height:114px">
    <h3>Education and Guidance</h3>
    <p>We endeavor to always be proactive in client education and guidance. This is achieved by our internal and external communications, comprehensive training programs and cross-departmental collaboration of knowledge sharing.</p>
  </article>

  <article class="cell cell--dark" style="left:173px;top:124px;width:170px;height:116px">
    <h3>Systems and processes</h3>
    <p>We strive to be the best in our field, by implementing efficiencies without compromising service quality, accuracy or compliance. We continually seek to achieve this by reviewing, updating and adopting continuous improvement strategies, systems and quality processes that deliver outcomes.</p>
  </article>
  <article class="cell cell--dark" style="left:173px;top:242px;width:170px;height:112px">
    <h3>Quality and Commitment</h3>
    <p>We invest in the recruitment and retention of a quality and diverse team of experienced professionals with a strong focus on continual professional development. As committed and skilled individuals, we actively promote the cross-departmental collaboration with one another to deliver a well rounded offering.</p>
  </article>
  <article class="cell cell--brown" style="left:173px;top:356px;width:170px;height:114px">
    <h3>Ethical Stance</h3>
    <p>We aim to create a community of ethical business relationships where we contribute our values and services to give our clients outstanding reassurance of our abilities.</p>
  </article>

  <div class="photo photo--keyboard" role="img" aria-label="Close-up photo of a keyboard with a pen" style="left:345px;top:124px;width:150px;height:76px"></div>
  <article class="cell cell--orange" style="left:345px;top:202px;width:150px;height:94px">
    <h3>Integrity</h3>
    <p>Our approach to strata management is bound by honesty and a strong set of moral principles. We act in our clients’ best interests with diligence and transparency for understanding and accountability.</p>
  </article>
  <div class="photo photo--city" role="img" aria-label="Photo of a city skyline with high-rise buildings" style="left:345px;top:298px;width:150px;height:172px"></div>

  <article class="cell cell--orange" style="left:497px;top:124px;width:193px;height:92px">
    <h3>Loyalty</h3>
    <p>We seek to develop a life-time relationship with our clients, building trust by acting with integrity, honesty and courtesy. We achieve this due to our expert approach to strata management and providing a responsive service to our clients.</p>
  </article>
  <article class="cell cell--dark cell--right" style="left:497px;top:218px;width:193px;height:88px">
    <h3>Continuous Improvement</h3>
    <p>Our goal is to continually evolve to better our offering and to be adaptable and responsive to change. Our infrastructure supports us to continually mould into the business that is right for our clients.</p>
  </article>
  <article class="cell cell--orange" style="left:497px;top:308px;width:193px;height:162px">
    <h3>Delivery</h3>
    <p>We empower our teams to deliver an outstanding client service and to be accountable for their actions. We will make sure every detail matters, provide valuable insight and supply information in a clear and timely manner.</p>
  </article>
</section>

<section class="flyer flyer--portrait" aria-label="Portrait principles flyer">
  <header class="masthead">
    <div class="brand">TenuraKeep</div>
    <h1 class="tagline">TenuraKeep is our principles of business that drive our people, systems and processes to give assurance to our clients that every detail matters.</h1>
  </header>

  <article class="cell cell--dark cell--right" style="left:0;top:124px;width:148px;height:118px">
    <h3>Client Experience</h3>
    <p>Our promise is to pursue excellence and to continually deliver a solutions based service. We achieve this through active engagement, open channels of communication and a serviced led team with the dedicated resources to listen, engage and implement.</p>
  </article>
  <article class="cell cell--orange" style="left:0;top:244px;width:148px;height:112px">
    <h3>Loyalty</h3>
    <p>We seek to develop a life-time relationship with our clients, building trust by acting with integrity, honesty and courtesy. We achieve this due to our expert approach to strata management and a responsive service to our clients.</p>
  </article>
  <article class="cell cell--orange cell--right" style="left:0;top:358px;width:148px;height:100px">
    <h3>Education and Guidance</h3>
    <p>We endeavor to always be proactive in client education and guidance. This is achieved by our internal and external communications, comprehensive training programs and cross-departmental collaboration of knowledge sharing.</p>
  </article>
  <article class="cell cell--brown" style="left:0;top:460px;width:148px;height:90px">
    <h3>Integrity</h3>
    <p>Our approach to strata management is bound by honesty and a strong set of moral principles. We act in our clients’ best interests with diligence and transparency for understanding and accountability.</p>
  </article>
  <article class="cell cell--orange" style="left:0;top:552px;width:148px;height:88px">
    <h3>Ethical Stance</h3>
    <p>We aim to create a community of ethical business relationships where we contribute our values and services to give our clients outstanding reassurance of our abilities.</p>
  </article>

  <article class="cell cell--dark" style="left:150px;top:124px;width:142px;height:124px">
    <h3>Continuous Improvement</h3>
    <p>Our goal is to continually evolve to better our offering and to be adaptable and responsive to change. Our infrastructure supports us to continually mould into the business that is right for our clients.</p>
  </article>
  <div class="photo photo--keyboard" role="img" aria-label="Close-up photo of a keyboard with a pen" style="left:150px;top:250px;width:142px;height:118px"></div>
  <article class="cell cell--orange cell--right" style="left:150px;top:370px;width:142px;height:96px">
    <h3>Delivery</h3>
    <p>We empower our teams to deliver an outstanding client service and to be accountable for their actions. We will make sure every detail matters, provide valuable insight and supply information in a clear and timely manner.</p>
  </article>
  <div class="photo photo--city" role="img" aria-label="Photo of a city skyline with high-rise buildings" style="left:150px;top:468px;width:142px;height:172px"></div>

  <article class="cell cell--dark" style="left:294px;top:124px;width:151px;height:200px">
    <h3>Compliance and Governance</h3>
    <p>We engage and own a position of ‘every detail matters’. We give due diligence to the relevant state and national legislations with which we, our clients and our stakeholders must comply. We regulate and achieve this through a robust system of internal processes and protocols which structure and confirm our deliverables are in line with regulations.</p>
  </article>
  <article class="cell cell--brown cell--right" style="left:294px;top:326px;width:151px;height:118px">
    <h3>Quality and Commitment</h3>
    <p>We invest in the recruitment and retention of a quality and diverse team of experienced professionals with a strong focus on continual professional development. As committed and skilled individuals, we actively promote the cross-departmental collaboration with one another to deliver a well rounded offering.</p>
  </article>
  <article class="cell cell--orange" style="left:294px;top:446px;width:151px;height:194px">
    <h3>Systems and processes</h3>
    <p>We strive to be the best in our field, by implementing efficiencies without compromising service quality, accuracy or compliance. We continually seek to achieve this by reviewing, updating and adopting continuous improvement strategies, systems and quality processes that deliver outcomes.</p>
  </article>
</section>

</body>
</html>
```